Plakat-Design für Gemeinschaftspraxis
Briefing
Ausgangssituation
Wir sind eine Gemeinschaftspraxis, die aus Ärzten und Physiotherapeuten besteht. Diese sollen unter einer gemeinsamen Marke präsentiert werden, dem sogenannten „Kelvaro“ (Farbcode Grün und Grau). Zusätzlich werden die Physiotherapeuten noch unter einer Marke zusammengefasst, dem sogenannten „Tesmunda“ (Farbcode Blau und Grün).
Kelvaro und Tesmunda haben jeweils eigene Internetseiten, Flyer und auch Visitenkarten.
Da jedoch beide Marken am selben Standort tätig sind, sollen auf diversen Plakaten (die im Umfeld der Ordination hängen werden) und den Schildern an der Türe auch beide Marken gemeinsam präsentiert werden.
Logos inkl. Farbrichtlinien wurden bereits gestaltet. Als Designvorlage dient ebenso ein allgemeiner Flyer über „Kelvaro“ (s. Anhang).
Im Anhang an das Briefing finden Sie alle relevanten Dateien wie Logos, Farbcodes, Fotos etc., die Sie zur Gestaltung der Werbemittel benötigen. Die grafische Umsetzung, Gliederung etc. überlassen wir Ihnen und freuen uns auf übersichtliche Vorschläge. Es wäre schön, wenn sich die Farbcodes der jeweiligen Marken auch in den Werbemitteln widerspiegeln. Wichtig ist uns, dass die Werbemittel klar und gut strukturiert gestaltet sind und nicht überladen wirken.
Hier finden Sie all mögliche Logo-Dateien, den bestehenden Flyer, die Farbwerte ,...
https://filedrop-example.net/t-Xq4bnLzPae
Farbregeln:
Wenn im Werbemittel nur ein Logo vorkommt, dann ist die Farbregel wie folgt:
Farbcode Kelvaro: Grün und Grau
Farbcode Tesmunda: Blau und Grün
Wenn im Werbemittel beide Logos vorkommen, dann ist die Farbregel wie folgt:
Farbcode Kelvaro: bleibt Grün und Grau
Farbcode Tesmunda: wird geändert in Blau und Grau
Viele der Werbemittel werden bei plakatfix.at produziert. Wenn Sie den jeweiligen Link beim Punkt „Datenaufbereitung“ anklicken, können Sie falls nötig auch direkt Formatvorlagen in diver..
Aufgabenstellung
Dieser Auftrag umfasst die Gestaltung von vier Plakaten in div. Größen mit identem Inhalt.
Bitte gestallten Sie zu Beginn nur die Größe 4000x1500cm
Sobald sich das Design in die richtige Richtung entwickelt, können dann auch die anderen Größen angelegt werden.
--> Bei zufriedenstellender Arbeit stehen eine Reihe von Folgeaufträgen an. (Siehe unten)
Plakate (4 Stück)
1. Plakat
Größe: 4000x1500cm
Info: Hängt zur Bewerbung der Praxis im Außenbereich an diversen Standorten in den umliegenden Orten, auf einer Höhe von ca. 3 Metern und soll vor allem vorbeifahrende Autofahrer ansprechen.
Inhalt:
Die Logos Kelvaro und Tesmunda
Die Adresse: Lindenhofweg 17/3, 2380 Perchtoldsdorf
E-Mailadressen office@kelvaro.net und office@tesmunda.at
Websites: www.kelvaro.net und www.tesmunda.at
Text: „Gemeinschaftspraxis für Orthopädie und Physiotherapie“
Fachbereiche/Schlagwörter: Unfallchirurgie, Sportmedizin, Rehabilitation, Sportphysiotherapie
Weitere optionale Schlagworte: Chiropraktik, Akupunktur, Prävention, Massagen
Datenaufbereitung:
Druckformat: 4060x1560mm
Sicherheitsabstand: 40mm
Abstand vom Ösenmittelpunkt zum Rand: 15mm
Abstand der Ösen zueinander: ca 500mm
Ösendurchmesser: 15mm
https://www.plakatfix.at/produkte/banner-transparente/transparente-planen-banner/
2. Plakat
Größe: 3000x1000mm
Inhalt/Info: identisch zu Plakat Nr. 1 4000x1500, nur das Format ist anders.
Druckformat: 3060x1060mm
3. Plakat
Größe: 4000x850mm
Info: Hängt auf der Fassade unseres Gebäudes und soll den Standort der Ordination klar kennzeichnen. Soll vorbeifahrende Autofahrer und Fußgänger auf die Ordinat..

```html
<!DOCTYPE html>
<html lang="de">
<head>
<meta charset="utf-8">
<title>Kelvaro & Tesmunda – Banner</title>
<link rel="stylesheet" href="https://fonts.googleapis.com/css2?family=Open+Sans:wght@400;600;700;800&display=swap">
<style>
  :root {
    --green: #6dbb35;
    --green-dark: #1f9a47;
    --grey: #6b6b6b;
    --grey-faint: #efefef;
    --grey-light: #ececec;
    --blue: #1f75c4;
    --paper: #f6f6f6;
    --stage: #e4e4e4;
  }
  * { margin: 0; padding: 0; box-sizing: border-box; }
  html, body { width: 1200px; height: 934px; overflow: hidden; }
  body {
    background: var(--stage);
    font-family: "Open Sans", Arial, sans-serif;
    position: relative;
  }
  .banner {
    position: absolute;
    left: 20px; top: 254px;
    width: 1160px; height: 426px;
    background: var(--paper);
    overflow: hidden;
  }
  .banner-shapes { position: absolute; inset: 0; }
  .intro {
    position: absolute; left: 45px; top: 38px;
    font-size: 26px; font-weight: 700; color: var(--grey);
  }
  .headline {
    position: absolute; left: 44px; top: 73px;
    font-size: 41px; font-weight: 800; color: var(--green);
    line-height: 48px;
  }
  .headline-rule {
    position: absolute; left: 45px; top: 176px;
    width: 458px; height: 6px;
    background: linear-gradient(90deg, var(--green-dark), var(--green));
  }
  .services {
    position: absolute; left: 45px; top: 196px;
    display: grid; grid-template-columns: 227px auto;
    row-gap: 2px;
    list-style: none;
    font-size: 24px; color: var(--grey);
  }
  .services li { position: relative; padding-left: 31px; line-height: 29px; }
  .services li::before {
    content: ""; position: absolute; left: 3px; top: 12px;
    width: 8px; height: 8px; border-radius: 50%; background: var(--green);
  }
  .address {
    position: absolute; left: 48px; top: 344px;
    display: flex; gap: 9px; align-items: flex-start;
    color: #fff; font-size: 18px; line-height: 22px;
  }
  .address svg { margin-top: 2px; flex: none; }
  .brand {
    position: absolute; top: 282px;
    display: flex; align-items: flex-end; gap: 8px;
    font-size: 27px; font-weight: 700; letter-spacing: 1px;
  }
  .brand-dot { width: 72px; height: 72px; border-radius: 50%; flex: none; }
  .brand--kelvaro { left: 352px; color: var(--green); }
  .brand--kelvaro .brand-dot { background: var(--green); }
  .brand--tesmunda { left: 593px; color: var(--blue); }
  .brand--tesmunda .brand-dot { background: var(--blue); }
  .brand-name { line-height: 34px; }
  .websites {
    position: absolute; right: 46px; top: 340px;
    text-align: right; font-size: 17px; font-weight: 700;
    color: var(--grey); line-height: 22px;
  }
</style>
</head>
<body>
  <section class="banner">
    <svg class="banner-shapes" width="1160" height="426" viewBox="0 0 1160 426">
      <defs>
        <linearGradient id="blobGradient" x1="0" y1="0" x2="1" y2="0">
          <stop offset="0" stop-color="#7dc242"/>
          <stop offset="1" stop-color="#1fae4b"/>
        </linearGradient>
        <linearGradient id="photoTone" x1="0" y1="0" x2="1" y2="1">
          <stop offset="0" stop-color="#c9b8a6"/>
          <stop offset="0.5" stop-color="#8a9099"/>
          <stop offset="1" stop-color="#4b79b4"/>
        </linearGradient>
        <clipPath id="photoClip"><circle cx="912" cy="34" r="248"/></clipPath>
      </defs>
      <circle class="deco-circle" cx="60" cy="110" r="292" fill="var(--grey-faint)"/>
      <circle class="deco-circle" cx="500" cy="220" r="126" fill="var(--grey-light)"/>
      <circle class="photo-accent" cx="900" cy="30" r="262" fill="var(--green)"/>
      <circle class="photo-gap" cx="912" cy="34" r="254" fill="#fff"/>
      <g clip-path="url(#photoClip)">
        <rect x="650" y="-220" width="520" height="520" fill="url(#photoTone)" role="img" aria-label="Fotocollage: Arzt erklärt ein Anatomiemodell, Physiotherapeut behandelt die Schulter eines älteren Patienten, Sporttherapie-Übung im hellen Trainingsraum"/>
      </g>
      <ellipse class="photo-cap" cx="1030" cy="-40" rx="205" ry="105" fill="var(--blue)"/>
      <path class="address-blob" d="M0 300 C70 312 130 322 210 306 C270 294 300 302 304 345 L300 426 L0 426 Z" fill="url(#blobGradient)"/>
    </svg>

    <p class="intro">GEMEINSCHAFTSPRAXIS FÜR</p>
    <h1 class="headline">ORTHOPÄDIE<br>UND PHYSIOTHERAPIE</h1>
    <div class="headline-rule"></div>
    <ul class="services">
      <li>Unfallchirurgie</li>
      <li>Rehabilitation</li>
      <li>Sportmedizin</li>
      <li>Sportphysiotherapie</li>
    </ul>

    <div class="address">
      <svg width="14" height="19" viewBox="0 0 14 19" aria-hidden="true">
        <path d="M7 0C3.1 0 0 3.1 0 7c0 5 7 12 7 12s7-7 7-12c0-3.9-3.1-7-7-7zm0 9.5A2.5 2.5 0 1 1 7 4.5a2.5 2.5 0 0 1 0 5z" fill="#fff"/>
      </svg>
      <p>Lindenhofweg 17 | TOP 3<br>3412 Kirchwalden</p>
    </div>

    <div class="brand brand--kelvaro">
      <span class="brand-name">KELVARO</span>
      <span class="brand-dot"></span>
    </div>
    <div class="brand brand--tesmunda">
      <span class="brand-name">TESMUNDA</span>
      <span class="brand-dot"></span>
    </div>

    <p class="websites">www.kelvaro.net<br>www.tesmunda.at</p>
  </section>
</body>
</html>
```